Lantern Advisory Website

I currently have a website www.lanternadvisoryinc.example. We are a IT Consulting Company. Our website will pretty much tell out our services. I am looking to enhance my website and make it look more professional. Looking for very classy and Contemporary look and design for my website.

It Company

```html
<!DOCTYPE html>
<html lang="en">
<head>
<meta charset="utf-8">
<title>Lantern Advisory</title>
<link href="https://fonts.googleapis.com/css2?family=Ubuntu:wght@400;500;700&family=Open+Sans:wght@400;600;700&display=swap" rel="stylesheet">
<style>
:root{
  --navy:#0b3b7c;
  --navy-dark:#072c61;
  --sky:#1aa1dc;
  --yellow:#f6d200;
  --orange:#ee5a24;
  --grey-bg:#e8e8e8;
  --card-bg:#f0f0f0;
  --text:#333;
  --muted:#8a8a8a;
  --footer:#2b2b2b;
  --white:#fff;
}
*{margin:0;padding:0;box-sizing:border-box}
html,body{width:1200px;height:4412px;overflow:hidden}
body{font-family:"Open Sans",Arial,sans-serif;color:var(--text);background:var(--white);position:relative}
h1,h2,h3,h4{font-family:"Ubuntu",Arial,sans-serif}
section,header,footer,.topbar{position:absolute;left:0;width:1200px}

.topbar{top:0;height:36px;background:var(--navy-dark);color:var(--white);font-size:13px;display:flex;align-items:center;padding-left:88px}
.topbar span{display:flex;align-items:center;gap:8px;margin-right:46px}
.topbar .office{position:absolute;right:50px;top:0;height:36px;width:154px;background:var(--yellow);color:var(--navy-dark);justify-content:center;margin:0}
.topbar svg{fill:var(--yellow)}

.site-header{top:36px;height:90px;background:rgba(255,255,255,.94);display:flex;align-items:center;padding:0 50px;z-index:2}
.brand{display:flex;align-items:center;gap:12px;font-family:"Ubuntu",sans-serif;font-weight:700;font-size:26px;color:var(--navy)}
.brand i{width:40px;height:40px;background:var(--sky);display:block}
.nav{margin-left:auto;display:flex;gap:40px;font-family:"Ubuntu",sans-serif;font-size:14px;font-weight:500;color:var(--navy-dark);text-transform:uppercase}
.nav a{padding:32px 0;border-bottom:4px solid transparent}
.nav a.active{border-color:var(--navy)}

.hero{top:36px;height:596px;background:linear-gradient(110deg,#c9d0d6 0%,#8a98a8 35%,#3d4a5c 60%,#2a3342 80%,#c7cdd3 100%)}
.quote-bar{top:632px;height:44px;background:var(--sky);color:var(--white);display:flex;align-items:center;padding:0 53px;font-size:20px}
.quote-bar .btn{margin-left:auto;background:var(--navy-dark);font-size:13px;font-weight:700;padding:8px 16px}

.features{top:726px;height:250px;display:flex;gap:38px;padding:0 53px}
.feature{flex:1;height:244px;position:relative;background:linear-gradient(135deg,#d8dde3,#7d8b9b)}
.feature .label{position:absolute;left:0;right:0;bottom:0;height:64px;background:rgba(11,59,124,.88);color:var(--white);display:flex;align-items:center;gap:14px;padding-left:22px;font-family:"Ubuntu",sans-serif;font-weight:700;font-size:19px}
.feature svg{fill:none;stroke:var(--yellow);stroke-width:3}

.services{top:1047px;height:526px;background:var(--grey-bg)}
.section-title{text-align:center;font-size:38px;font-weight:700;color:var(--navy-dark)}
.section-title::after{content:"";display:block;width:56px;height:4px;background:var(--yellow);margin:14px auto 0}
.services .section-title{margin-top:24px}
.service-grid{display:grid;grid-template-columns:repeat(3,340px);column-gap:60px;row-gap:92px;padding:50px 0 0 60px}
.service{display:flex;gap:18px}
.service .ico{flex:none;width:46px;height:46px;border-radius:50%;background:var(--navy);display:flex;align-items:center;justify-content:center}
.service .ico svg{stroke:var(--white);fill:none;stroke-width:2}
.service h3{font-size:18px;font-weight:700;color:var(--navy-dark);margin-bottom:8px}
.service p{font-size:14px;line-height:22px;color:#555}

.banner{top:1573px;height:212px;background:var(--navy);text-align:center;font-family:"Ubuntu",sans-serif;font-weight:700;font-size:31px;text-transform:uppercase;line-height:46px;padding-top:56px;color:var(--white)}
.banner em{font-style:normal;color:var(--yellow);display:block}

.news{top:1785px;height:582px}
.news .section-title{margin-top:52px}
.news-row{display:flex;gap:36px;padding:0 46px;margin-top:56px}
.news-card{flex:1;display:flex;height:268px}
.news-card .body{flex:1;background:var(--card-bg);margin-top:38px;height:200px;padding:30px 30px}
.news-card h4{font-weight:500;color:var(--sky);font-size:19px;margin-bottom:12px}
.news-card p{font-size:14px;line-height:22px;color:var(--muted)}
.news-card .more{font-size:14px;color:#555;margin-top:16px;display:block}
.news-card .pic{width:252px;position:relative;background:linear-gradient(135deg,#e6e8ea,#a9b3bc)}
.news-card .date{position:absolute;left:0;top:0;width:66px;height:66px;background:var(--orange);color:var(--white);text-align:center;font-size:12px;font-weight:700;padding-top:14px;line-height:18px}
.dots{display:flex;justify-content:center;gap:10px;margin-top:58px}
.dots i{width:18px;height:18px;border-radius:50%;background:#bbb}
.dots i:first-child{background:var(--navy)}

.solutions{top:2367px;height:564px;background:var(--navy);color:var(--white)}
.solutions .section-title{color:var(--white);margin-top:30px}
.sol-row{display:flex;gap:44px;padding:0 47px;margin-top:40px}
.sol{flex:1}
.sol .pic{height:192px;background:linear-gradient(135deg,#f2f3f4,#b3bcc6)}
.sol h3{font-size:25px;font-weight:500;margin:20px 0 10px}
.sol p{font-size:14px;line-height:20px;text-align:justify}
.sol .btn{display:inline-block;border:2px solid var(--yellow);padding:9px 18px;font-size:14px;font-weight:600;margin-top:18px}

.testimonials{top:2931px;height:559px;text-align:center}
.testimonials .section-title{margin-top:34px}
.quote-mark{width:58px;height:58px;border-radius:50%;border:2px solid var(--orange);margin:48px auto 26px;color:var(--orange);font-family:Georgia,serif;font-size:40px;line-height:64px}
.testimonials p{width:1020px;margin:0 auto;font-size:14px;line-height:26px;color:#666}
.testimonials .by{font-size:12px;color:#666;margin-top:22px}
.testimonials .name{font-family:"Ubuntu",sans-serif;font-weight:700;color:var(--navy);font-size:15px;margin-top:6px}
.avatars{position:relative;width:112px;height:112px;margin:22px auto 0}
.avatars i{position:absolute;width:48px;height:48px;border-radius:50%;background:linear-gradient(135deg,#d9b7a2,#8a6b5b)}

.map{top:3490px;height:338px;background:linear-gradient(160deg,#e9eef0,#d7e3d7 50%,#e8edf0)}

.offices{top:3828px;height:282px;background:var(--navy);display:flex;padding:50px 0 0 0;color:var(--white)}
.office-col{flex:1;padding-left:92px;border-right:1px solid rgba(255,255,255,.35);height:180px}
.office-col:last-child{border:none;padding-left:92px}
.office-col:first-child{padding-left:92px}
.office-col h3{font-size:29px;font-weight:500;margin-bottom:16px}
.office-col li{list-style:none;display:flex;gap:14px;font-size:14px;font-weight:600;line-height:19px;margin-bottom:18px}
.office-col svg{fill:var(--yellow);flex:none}

.site-footer{top:4110px;height:302px;background:var(--footer);color:var(--white);text-align:center}
.site-footer .brand{justify-content:center;color:var(--white);margin-top:42px}
.site-footer .brand i{background:var(--white)}
.footer-nav{font-size:15px;margin-top:36px;letter-spacing:.5px}
.copy{font-size:14px;margin-top:8px}
.social{display:flex;justify-content:center;gap:18px;margin-top:30px}
.social i{width:34px;height:34px;background:var(--white);transform:rotate(45deg)}
</style>
</head>
<body>

<div class="topbar">
  <span>English ▾</span>
  <span><svg width="12" height="16" viewBox="0 0 12 16"><path d="M6 0a6 6 0 0 0-6 6c0 4.5 6 10 6 10s6-5.5 6-10a6 6 0 0 0-6-6zm0 8.5A2.5 2.5 0 1 1 6 3.5a2.5 2.5 0 0 1 0 5z"/></svg>1010 Harbor Lane, New York, NY 10018 US.</span>
  <span><svg width="14" height="14" viewBox="0 0 14 14"><circle cx="7" cy="7" r="6" fill="none" stroke="#f6d200" stroke-width="2"/><path d="M7 3v4h3" stroke="#f6d200" stroke-width="2" fill="none"/></svg>Mon - Sat 8.00 - 18.00. Sunday CLOSED</span>
  <span><svg width="14" height="14" viewBox="0 0 14 14"><path d="M3 0l3 3-2 2c1 2 3 4 5 5l2-2 3 3-2 3C6 14 0 8 0 3z"/></svg>212 555 0175</span>
  <span class="office">New York Office ▾</span>
</div>

<section class="hero" role="img" aria-label="Photo of two businessmen in suits smiling over a laptop in an office"></section>

<header class="site-header">
  <div class="brand"><i></i>Lantern Advisory</div>
  <nav class="nav">
    <a class="active">Company</a><a>Services</a><a>Solutions</a><a>Resources</a><a>Career</a><a>Contact Us</a>
  </nav>
</header>

<section class="quote-bar">Looking for a First-Class Business Consultant?<span class="btn">get a quote ›</span></section>

<section class="features">
  <div class="feature" role="img" aria-label="Photo of hands signing a business document">
    <div class="label"><svg width="30" height="28" viewBox="0 0 30 28"><circle cx="15" cy="7" r="5"/><path d="M5 27v-7a10 8 0 0 1 20 0v7"/></svg>Our Mission</div>
  </div>
  <div class="feature" role="img" aria-label="Photo of a business team meeting around a table">
    <div class="label"><svg width="34" height="24" viewBox="0 0 34 24"><path d="M2 12C8 2 26 2 32 12 26 22 8 22 2 12z"/><circle cx="17" cy="12" r="5"/></svg>Our Vision</div>
  </div>
  <div class="feature" role="img" aria-label="Photo of colleagues reviewing work together">
    <div class="label"><svg width="28" height="28" viewBox="0 0 28 28"><rect x="3" y="3" width="22" height="22"/><circle cx="14" cy="14" r="5"/></svg>Quality Focus</div>
  </div>
</section>

<section class="services">
  <h2 class="section-title">Our Services</h2>
  <div class="service-grid">
    <div class="service"><div class="ico"><svg width="24" height="24" viewBox="0 0 24 24"><circle cx="12" cy="12" r="4"/><path d="M12 2v4M12 18v4M2 12h4M18 12h4"/></svg></div><div><h3>Technology</h3><p>Company that offers design and build services for you from initial sketches to the final production.</p></div></div>
    <div class="service"><div class="ico"><svg width="24" height="24" viewBox="0 0 24 24"><rect x="3" y="7" width="18" height="13"/><path d="M9 7V4h6v3"/></svg></div><div><h3>Business</h3><p>Company that offers design and build services for you from initial sketches to the final production.</p></div></div>
    <div class="service"><div class="ico"><svg width="24" height="24" viewBox="0 0 24 24"><rect x="4" y="3" width="16" height="18"/><path d="M8 9h8M8 13h8M8 17h5"/></svg></div><div><h3>Application Developement</h3><p>Company that offers design and build services for you from initial sketches to the final production.</p></div></div>
    <div class="service"><div class="ico"><svg width="24" height="24" viewBox="0 0 24 24"><path d="M4 20l6-6M14 10l6-6M8 4h12v12"/></svg></div><div><h3>Enterprise Integration</h3><p>Company that offers design and build services for you from initial sketches to the final production.</p></div></div>
    <div class="service"><div class="ico"><svg width="24" height="24" viewBox="0 0 24 24"><circle cx="12" cy="8" r="4"/><path d="M5 21a7 7 0 0 1 14 0"/></svg></div><div><h3>IT Consulting</h3><p>Company that offers design and build services for you from initial sketches to the final production.</p></div></div>
    <div class="service"><div class="ico"><svg width="24" height="24" viewBox="0 0 24 24"><rect x="3" y="4" width="18" height="12"/><path d="M8 20h8M12 16v4"/></svg></div><div><h3>Staff Augmentation</h3><p>Company that offers design and build services for you from initial sketches to the final production.</p></div></div>
  </div>
</section>

<section class="banner"><em>To help entrepreneurs get their act together</em>before they talk to investors.</section>

<section class="news">
  <h2 class="section-title">NEWS</h2>
  <div class="news-row">
    <article class="news-card">
      <div class="body"><h4>News Heading</h4><p>There are many variations of passages of Lorem Ipsum available majority have suffered...</p><span class="more">Read More →</span></div>
      <div class="pic" role="img" aria-label="Photo of two colleagues working at a whiteboard"><span class="date">29<br>NOV</span></div>
    </article>
    <article class="news-card">
      <div class="body"><h4>News Heading</h4><p>If people are really excited about their music, and that's their primary motivation...</p><span class="more">Read More →</span></div>
      <div class="pic" role="img" aria-label="Photo of a business handshake"><span class="date">29<br>NOV</span></div>
    </article>
  </div>
  <div class="dots"><i></i><i></i><i></i></div>
</section>

<section class="solutions">
  <h2 class="section-title">Solutions</h2>
  <div class="sol-row">
    <div class="sol"><div class="pic" role="img" aria-label="Photo of a man working at a desktop computer"></div><h3>Dashbords</h3><p>Our Offshore Development Center at Hyderabad, India is comprised of an excellent delivery facility and staff dedicated to our customer's IT requirements. The center consists of a team...</p><span class="btn">Read More</span></div>
    <div class="sol"><div class="pic" role="img" aria-label="Photo of a man reviewing papers at a laptop"></div><h3>Data Warehousing</h3><p>Our Offshore Development Center at Hyderabad, India is comprised of an excellent delivery facility and staff dedicated to our customer's IT requirements. The center consists of a team...</p><span class="btn">Read More</span></div>
    <div class="sol"><div class="pic" role="img" aria-label="Photo of a woman working at a bright office desk"></div><h3>BPM</h3><p>Our Offshore Development Center at Hyderabad, India is comprised of an excellent delivery facility and staff dedicated to our customer's IT requirements. The center consists of a team...</p><span class="btn">Read More</span></div>
  </div>
</section>

<section class="testimonials">
  <h2 class="section-title">Tesimonials</h2>
  <div class="quote-mark">“</div>
  <p>Lorem Ipsum is simply dummy text of the printing and typesetting industry. Lorem Ipsum has been the industry's standard dummy text ever since the 1500s, when an unknown printer took a galley of type and scrambled it to make a type specimen book. It has survived not only five centuries, but also the leap into electronic typesetting, remaining essentially unchanged.</p>
  <div class="by">By</div>
  <div class="name">DR. ARLEN</div>
  <div class="avatars" role="img" aria-label="Cluster of five client portrait photos">
    <i style="left:0;top:0"></i><i style="left:32px;top:0;background:linear-gradient(135deg,#f08a4b,#c0522a)"></i><i style="left:64px;top:0"></i><i style="left:16px;top:56px"></i><i style="left:50px;top:56px"></i>
  </div>
</section>

<section class="map" role="img" aria-label="Street map showing the office location with a red pin"></section>

<section class="offices">
  <div class="office-col"><h3>Head Office</h3><ul>
    <li><svg width="12" height="16" viewBox="0 0 12 16"><path d="M6 0a6 6 0 0 0-6 6c0 4.5 6 10 6 10s6-5.5 6-10a6 6 0 0 0-6-6zm0 8.5A2.5 2.5 0 1 1 6 3.5a2.5 2.5 0 0 1 0 5z"/></svg>1001 Example Ave<br>Suite 205</li>
    <li><svg width="14" height="14" viewBox="0 0 14 14"><rect x="1" y="1" width="12" height="12"/></svg>Northfield, NJ 07000</li>
    <li><svg width="14" height="14" viewBox="0 0 14 14"><path d="M3 0l3 3-2 2c1 2 3 4 5 5l2-2 3 3-2 3C6 14 0 8 0 3z"/></svg>Phone: +1 (732) 555 0143</li></ul></div>
  <div class="office-col"><h3>Head Office</h3><ul>
    <li><svg width="12" height="16" viewBox="0 0 12 16"><path d="M6 0a6 6 0 0 0-6 6c0 4.5 6 10 6 10s6-5.5 6-10a6 6 0 0 0-6-6zm0 8.5A2.5 2.5 0 1 1 6 3.5a2.5 2.5 0 0 1 0 5z"/></svg>1001 Example Ave<br>Suite 205</li>
    <li><svg width="14" height="14" viewBox="0 0 14 14"><rect x="1" y="1" width="12" height="12"/></svg>Northfield, NJ 07000</li>
    <li><svg width="14" height="14" viewBox="0 0 14 14"><path d="M3 0l3 3-2 2c1 2 3 4 5 5l2-2 3 3-2 3C6 14 0 8 0 3z"/></svg>Phone: +1 (732) 555 0143</li></ul></div>
  <div class="office-col"><h3>Head Office</h3><ul>
    <li><svg width="12" height="16" viewBox="0 0 12 16"><path d="M6 0a6 6 0 0 0-6 6c0 4.5 6 10 6 10s6-5.5 6-10a6 6 0 0 0-6-6zm0 8.5A2.5 2.5 0 1 1 6 3.5a2.5 2.5 0 0 1 0 5z"/></svg>1001 Example Ave<br>Suite 205</li>
    <li><svg width="14" height="14" viewBox="0 0 14 14"><rect x="1" y="1" width="12" height="12"/></svg>Northfield, NJ 07000</li>
    <li><svg width="14" height="14" viewBox="0 0 14 14"><path d="M3 0l3 3-2 2c1 2 3 4 5 5l2-2 3 3-2 3C6 14 0 8 0 3z"/></svg>Phone: +1 (732) 555 0143</li></ul></div>
</section>

<footer class="site-footer">
  <div class="brand"><i></i>Lantern Advisory</div>
  <div class="footer-nav">HOME - SOLUTIONS - SERVICES - COMPANY - CONTACT</div>
  <div class="copy">Copyright © 2007 - 2015 Lantern Advisory, Inc. All Rights Reserved</div>
  <div class="social"><i></i><i></i><i></i><i></i></div>
</footer>

</body>
</html>
```